Company selling food supplements with CBD needs label.

We need a label design for a company called "VEX Lab ltd", is based in the UK, the market name is "VEX" or "VEX Velvet Ember Xtracts". The initial product is Virgin Organic Hemp Seed Oil with a CBD in a 10ml amber dropper bottle. The design should be simplicity and luxury. The design should include also box.

Target Market(s)

Food supplements on Pellmart UK

Industry/Entity Type

Supplement

Font styles to use
Other font styles liked:
• Some luxury

Colors

Designer to choose colors to be used in the design.

Requirements
Must have
• All the information on the label required by the UK for the food supplements, the same on the box. One version matt one transparent. The design should include different CBD content, one different bottle (250mg, 500mg, 750mg, 1000mg) .
• The label and box should include the following phrases: "DIRECTIONS: Food Supplement. Shake well before use. Use 4-6 drops 2-3 times a day. Leave the oil in your mouth for 30-60 seconds before swallowing. Gradually build up the dose to find your optimum dosage.
• CAUTION: Do not exceed the recommended daily intake. Do not use as a substitute for a varied diet. Do not use during pregnancy and breastfeeding. Store in a dark and cool place, away from sunlight. Keep away from children.
• INGREDIENTS: Hemp Seed Oil, Omega-6 (2800mg), Omega-3 (930mg), CBD (250mg)
• MANUFACTURED: VEX Lab Ltd, 87 Quillon Rd, Harrow, KT9 4PW, www,vexlabuk.co.uk, info@vexlabuk.co.uk.
• EXPIRED DATE: "
• The box should also include a place for bark code.
Nice to have
• Simple and elegant design vertical or horizontal with exposed company logo "VEX" or "VEX Velvet Ember Xtracts". The company logo is provided but designers may change it freely.
Should not have
• The best without pictures/graphics overloading simplicity and purity of design.

```html
<!DOCTYPE html>
<html lang="en">
<head>
<meta charset="utf-8">
<title>VEX Hemp Seed Oil – Box Dieline</title>
<link rel="stylesheet" href="https://fonts.googleapis.com/css2?family=Oswald:wght@300;400;500&family=Ubuntu:wght@400&family=Quicksand:wght@600&family=Open+Sans:wght@700&display=swap">
<style>
  :root {
    --keyline: #2ee6f0;
    --panel-tint: #e2fbd0;
    --pantone-368: #66ff00;
    --pantone-355: #00f00d;
    --heading-green: #2fc41f;
    --leaf-green: #7fe61f;
    --ink: #111111;
    --paper: #ffffff;
  }
  html, body { margin: 0; padding: 0; width: 918px; height: 1200px; overflow: hidden; background: var(--paper); }
  .dieline { display: block; width: 918px; height: 1200px; }
  .cut { fill: none; stroke: var(--keyline); stroke-width: 1.6; }
  .dim-line { stroke: var(--keyline); stroke-width: 1.4; fill: none; }
  .dim-label { font-family: 'Ubuntu', sans-serif; fill: var(--keyline); }
  .dim-title { font-size: 50px; }
  .dim-big { font-size: 72px; }
  .dim-small { font-size: 50px; }
  .tint { fill: var(--panel-tint); }
  .band-light { fill: var(--pantone-368); }
  .band-deep { fill: var(--pantone-355); }
  .brand-name { font-family: 'Oswald', sans-serif; font-weight: 500; fill: var(--ink); }
  .brand-tagline { font-family: 'Oswald', sans-serif; font-weight: 300; fill: var(--ink); }
  .product-name { font-family: 'Quicksand', sans-serif; font-weight: 600; font-size: 17px; fill: var(--ink); }
  .strength-bar { fill: var(--pantone-368); }
  .strength-text { font-family: 'Open Sans', sans-serif; font-weight: 700; font-size: 17px; fill: var(--paper); }
  .info-heading { font-family: 'Oswald', sans-serif; font-weight: 300; font-size: 19px; fill: var(--heading-green); }
  .info-body { font-family: 'Oswald', sans-serif; font-weight: 300; font-size: 19.5px; fill: var(--ink); }
  .info-dose { font-family: 'Oswald', sans-serif; font-weight: 300; font-size: 23px; fill: var(--ink); }
  .barcode-frame { fill: var(--paper); stroke: var(--keyline); stroke-width: 1.4; }
  .barcode-label { font-family: 'Ubuntu', sans-serif; font-size: 24px; fill: #c9f6f8; letter-spacing: 2px; }
  .guide-title { font-family: 'Oswald', sans-serif; font-weight: 300; font-size: 24px; fill: var(--ink); }
  .guide-label { font-family: 'Oswald', sans-serif; font-weight: 300; font-size: 24px; fill: var(--ink); }
  .swatch-keyline { fill: #00f5ff; }
  .swatch-black { fill: #000000; }
</style>
</head>
<body>
<svg class="dieline" viewBox="0 0 1683 2200" xmlns="http://www.w3.org/2000/svg">
  <defs>
    <radialGradient id="leafFill" cx="50%" cy="50%" r="50%">
      <stop offset="0%" stop-color="#7fe61f"/>
      <stop offset="70%" stop-color="#9bf04a" stop-opacity="0.85"/>
      <stop offset="100%" stop-color="#e2fbd0" stop-opacity="0"/>
    </radialGradient>
    <radialGradient id="leafFaint" cx="50%" cy="50%" r="50%">
      <stop offset="0%" stop-color="#e4f8d2"/>
      <stop offset="100%" stop-color="#ffffff" stop-opacity="0"/>
    </radialGradient>
  </defs>

  <!-- Dimensions -->
  <g class="dimensions">
    <text class="dim-label dim-title" x="273" y="93">All dimensions in mm</text>
    <text class="dim-label dim-big" x="828" y="184" text-anchor="middle">155</text>
    <line class="dim-line" x1="272" y1="235" x2="1381" y2="235"/>
    <line class="dim-line" x1="272" y1="182" x2="272" y2="288"/>
    <line class="dim-line" x1="1381" y1="182" x2="1381" y2="288"/>

    <line class="dim-line" x1="163" y1="343" x2="163" y2="1845"/>
    <line class="dim-line" x1="110" y1="343" x2="218" y2="343"/>
    <line class="dim-line" x1="110" y1="1845" x2="218" y2="1845"/>
    <text class="dim-label dim-big" transform="translate(90,943) rotate(-90)" text-anchor="middle">210</text>

    <line class="dim-line" x1="1488" y1="343" x2="1488" y2="1845"/>
    <g>
      <line class="dim-line" x1="1435" y1="343" x2="1543" y2="343"/>
      <line class="dim-line" x1="1435" y1="432" x2="1543" y2="432"/>
      <line class="dim-line" x1="1435" y1="500" x2="1543" y2="500"/>
      <line class="dim-line" x1="1435" y1="679" x2="1543" y2="679"/>
      <line class="dim-line" x1="1435" y1="1502" x2="1543" y2="1502"/>
      <line class="dim-line" x1="1435" y1="1681" x2="1543" y2="1681"/>
      <line class="dim-line" x1="1435" y1="1749" x2="1543" y2="1749"/>
      <line class="dim-line" x1="1435" y1="1845" x2="1543" y2="1845"/>
    </g>
    <text class="dim-label dim-small" x="1522" y="412">12.5</text>
    <text class="dim-label dim-small" x="1522" y="480">9.5</text>
    <text class="dim-label dim-small" x="1522" y="617">25</text>
    <text class="dim-label dim-small" x="1522" y="1003">115</text>
    <text class="dim-label dim-small" x="1522" y="1617">25</text>
    <text class="dim-label dim-small" x="1522" y="1730">9.5</text>
    <text class="dim-label dim-small" x="1522" y="1822">12.5</text>

    <line class="dim-line" x1="272" y1="1952" x2="1381" y2="1952"/>
    <line class="dim-line" x1="272" y1="1900" x2="272" y2="2005"/>
    <line class="dim-line" x1="378" y1="1900" x2="378" y2="2005"/>
    <line class="dim-line" x1="629" y1="1900" x2="629" y2="2005"/>
    <line class="dim-line" x1="880" y1="1900" x2="880" y2="2005"/>
    <line class="dim-line" x1="1130" y1="1900" x2="1130" y2="2005"/>
    <line class="dim-line" x1="1381" y1="1900" x2="1381" y2="2005"/>
    <text class="dim-label dim-small" x="322" y="2026" text-anchor="middle">15</text>
    <text class="dim-label dim-small" x="480" y="2026" text-anchor="middle">35</text>
    <text class="dim-label dim-small" x="753" y="2026" text-anchor="middle">35</text>
    <text class="dim-label dim-small" x="1026" y="2026" text-anchor="middle">35</text>
    <text class="dim-label dim-small" x="1298" y="2026" text-anchor="middle">35</text>
  </g>

  <!-- Tinted panels -->
  <g class="panel-tints">
    <rect class="tint" x="378" y="322" width="251" height="1180"/>
    <rect class="tint" x="880" y="683" width="250" height="1177"/>
  </g>

  <!-- Colour bands -->
  <rect class="band-light" x="378" y="1432" width="1024" height="35"/>
  <rect class="band-deep" x="378" y="1467" width="1024" height="35"/>

  <!-- Cut and fold lines -->
  <g class="cut-lines">
    <rect class="cut" x="378" y="683" width="1003" height="819"/>
    <line class="cut" x1="629" y1="683" x2="629" y2="1502"/>
    <line class="cut" x1="880" y1="683" x2="880" y2="1502"/>
    <line class="cut" x1="1130" y1="683" x2="1130" y2="1502"/>
    <path class="cut" d="M378,683 L272,717 L272,1470 L378,1502"/>
    <path class="cut" d="M378,683 V380 Q378,343 415,343 H592 Q629,343 629,380 V683"/>
    <line class="cut" x1="378" y1="432" x2="629" y2="432"/>
    <path class="cut" d="M629,683 L665,648 V503 H845 L880,648 V683"/>
    <path class="cut" d="M1130,683 V648 L1166,503 H1345 V648 L1381,683"/>
    <path class="cut" d="M629,1502 V1542 L665,1685 H845 V1540 L880,1502"/>
    <path class="cut" d="M1130,1502 L1166,1540 V1685 H1345 L1381,1542 V1502"/>
    <path class="cut" d="M880,1502 V1808 Q880,1845 917,1845 H1093 Q1130,1845 1130,1808 V1502"/>
    <line class="cut" x1="880" y1="1755" x2="1130" y2="1755"/>
  </g>

  <!-- Top tuck flap -->
  <g class="tuck-flap">
    <g transform="translate(503,560) rotate(180)">
      <text class="brand-name" x="0" y="34" font-size="92" text-anchor="middle" textLength="182" lengthAdjust="spacingAndGlyphs">VEX</text>
      <text class="brand-tagline" x="0" y="57" font-size="13" text-anchor="middle" letter-spacing="1.5">Velvet Ember Xtracts</text>
    </g>
    <rect role="img" aria-label="Small hemp leaf illustration" x="392" y="602" width="76" height="80" rx="30" fill="url(#leafFill)"/>
  </g>

  <!-- Front panel -->
  <g class="front-panel">
    <rect role="img" aria-label="Hemp leaf illustration" x="432" y="820" width="186" height="170" rx="80" fill="url(#leafFill)"/>
    <text class="brand-name" transform="translate(513,1310) rotate(-90)" x="0" y="0" font-size="150" textLength="305" lengthAdjust="spacingAndGlyphs">VEX</text>
    <text class="brand-tagline" transform="translate(543,1310) rotate(-90)" x="0" y="0" font-size="22" textLength="303" lengthAdjust="spacing">Velvet Ember Xtracts</text>
    <rect class="strength-bar" x="575" y="1107" width="26" height="203"/>
    <text class="strength-text" transform="translate(594,1304) rotate(-90)">CBD 250mg</text>
    <text class="product-name" x="398" y="1358" textLength="204" lengthAdjust="spacingAndGlyphs">Virgin Organic Hemp Seed OIL</text>
  </g>

  <!-- Directions panel -->
  <g class="directions-panel">
    <text class="info-heading" x="658" y="723">DIRECTIONS:</text>
    <text class="info-body" x="658" y="747">Food Supplement. Shake well</text>
    <text class="info-body" x="658" y="771">before use. Use 4-6 drops 2-3</text>
    <text class="info-body" x="658" y="795">times a day. Leave the oil in</text>
    <text class="info-body" x="658" y="819">your mouth for 30-60 seconds</text>
    <text class="info-body" x="658" y="843">before swallowing. Gradually</text>
    <text class="info-body" x="658" y="867">build up the dose to find your</text>
    <text class="info-body" x="658" y="891">optimum dosage.</text>
    <text class="info-dose" x="666" y="927">1mg/drop</text>
    <text class="info-dose" x="782" y="927">30 ml</text>
    <rect role="img" aria-label="Faint hemp leaf decoration" x="676" y="948" width="182" height="165" rx="80" fill="url(#leafFaint)"/>
    <rect class="barcode-frame" x="680" y="1136" width="149" height="272"/>
    <text class="barcode-label" transform="translate(761,1326) rotate(-90)">BARCODE</text>
  </g>

  <!-- Back panel (front repeat) -->
  <g class="back-panel">
    <rect role="img" aria-label="Hemp leaf illustration" x="940" y="820" width="186" height="170" rx="80" fill="url(#leafFill)"/>
    <text class="brand-name" transform="translate(1021,1310) rotate(-90)" x="0" y="0" font-size="150" textLength="305" lengthAdjust="spacingAndGlyphs">VEX</text>
    <text class="brand-tagline" transform="translate(1051,1310) rotate(-90)" x="0" y="0" font-size="22" textLength="303" lengthAdjust="spacing">Velvet Ember Xtracts</text>
    <rect class="strength-bar" x="1083" y="1107" width="26" height="203"/>
    <text class="strength-text" transform="translate(1102,1304) rotate(-90)">CBD 250mg</text>
    <text class="product-name" x="906" y="1358" textLength="204" lengthAdjust="spacingAndGlyphs">Virgin Organic Hemp Seed OIL</text>
  </g>

  <!-- Information panel -->
  <g class="information-panel">
    <text class="info-heading" x="1157" y="743">INGREDIENTS:</text>
    <text class="info-body" x="1157" y="767">Hemp Seed Oil, Omega-6</text>
    <text class="info-body" x="1157" y="791">(2800mg), Omega-3 (930mg),</text>
    <text class="info-body" x="1157" y="815">CBD (250mg)</text>

    <text class="info-heading" x="1155" y="893">CAUTION:</text>
    <text class="info-body" x="1155" y="917" textLength="211" lengthAdjust="spacingAndGlyphs">Do not exceed the recommended</text>
    <text class="info-body" x="1155" y="941">daily intake.</text>
    <text class="info-body" x="1155" y="965" textLength="204" lengthAdjust="spacingAndGlyphs">Do not use as a substitute for a</text>
    <text class="info-body" x="1155" y="989">varied diet.</text>
    <text class="info-body" x="1155" y="1013" textLength="213" lengthAdjust="spacingAndGlyphs">Do not use during pregnancy and</text>
    <text class="info-body" x="1155" y="1037">breastfeeding.</text>
    <text class="info-body" x="1155" y="1083">Store in a dark and cool place,</text>
    <text class="info-body" x="1155" y="1107">away from sunlight. Keep away</text>
    <text class="info-body" x="1155" y="1131">from children.</text>

    <text class="info-heading" x="1153" y="1215">MANUFACTURED:</text>
    <text class="info-body" x="1153" y="1239">VEX Lab Ltd, 87 Quillon Rd,</text>
    <text class="info-body" x="1153" y="1263">Harrow, KT9 4PW,</text>
    <text class="info-body" x="1153" y="1287">www,vexlabuk.co.uk,</text>
    <text class="info-body" x="1153" y="1311">info@vexlabuk.co.uk.</text>

    <text class="info-body" x="1157" y="1357">EXPIRED DATE:</text>
    <text class="info-body" x="1157" y="1381">BATCH NO:</text>
  </g>

  <!-- Bottom tuck flap -->
  <g class="tuck-flap">
    <g transform="translate(1012,1610) rotate(180)">
      <text class="brand-name" x="0" y="34" font-size="92" text-anchor="middle" textLength="182" lengthAdjust="spacingAndGlyphs">VEX</text>
      <text class="brand-tagline" x="0" y="57" font-size="13" text-anchor="middle" letter-spacing="1.5">Velvet Ember Xtracts</text>
    </g>
    <rect role="img" aria-label="Small hemp leaf illustration" x="902" y="1652" width="76" height="80" rx="30" fill="url(#leafFill)"/>
  </g>

  <!-- Colour guide -->
  <g class="colour-guide">
    <text class="guide-title" x="273" y="2070">COLOUR GUIDE</text>
    <rect class="band-deep" x="272" y="2102" width="35" height="36"/>
    <text class="guide-label" x="317" y="2140">PANTONE 355 C</text>
    <rect class="band-light" x="499" y="2102" width="35" height="36"/>
    <text class="guide-label" x="544" y="2140">PANTONE 368 C</text>
    <rect class="swatch-black" x="726" y="2102" width="35" height="36"/>
    <text class="guide-label" x="770" y="2140">BLACK</text>
    <rect class="swatch-keyline" x="1113" y="2102" width="35" height="36"/>
    <text class="guide-label" x="1165" y="2140">KEY LINES</text>
  </g>
</svg>
</body>
</html>
```